Veltrano - Mechanic/Collision Center Business Card

We're looking for a business card design for our mechanic/ collision repair shop.

Can be with colours or monochromatic.

See the attached files.

Many thanks

```html
<!DOCTYPE html>
<html lang="en">
<head>
<meta charset="utf-8">
<title>Veltrano – Business Card</title>
<link href="https://fonts.googleapis.com/css2?family=Roboto:wght@400;500;700;900&display=swap" rel="stylesheet">
<style>
  :root{
    --backdrop:#808080;
    --card-white:#ffffff;
    --brand-blue:#1e9fda;
    --ink:#1f2328;
    --text:#222428;
  }
  html,body{margin:0;padding:0;}
  body{
    width:1200px;height:1020px;overflow:hidden;
    background:var(--backdrop);
    font-family:"Roboto",Arial,sans-serif;
    position:relative;
  }
  .card{
    position:absolute;left:272px;width:657px;height:377px;
    border-radius:23px;overflow:hidden;
  }
  .card--front{top:87px;background:var(--card-white);}
  .card--back{top:514px;background:var(--brand-blue);}

  .accent-bar{position:absolute;left:0;top:79px;width:10px;height:43px;background:var(--brand-blue);}
  .person-name{position:absolute;left:22px;top:72px;margin:0;font-size:27px;font-weight:500;color:var(--brand-blue);line-height:1.2;}
  .person-role{position:absolute;left:22px;top:106px;margin:0;font-size:18px;font-weight:400;color:var(--text);line-height:1.2;}

  .brand{
    position:absolute;display:flex;align-items:center;gap:10px;
    font-weight:900;color:var(--ink);letter-spacing:.5px;
  }
  .brand__dot{border-radius:50%;background:var(--brand-blue);flex:none;}
  .card--front .brand{right:26px;top:58px;font-size:42px;}
  .card--front .brand__dot{width:22px;height:22px;}
  .card--back .brand{left:0;right:0;top:150px;justify-content:center;font-size:74px;gap:16px;}
  .card--back .brand__dot{width:34px;height:34px;background:var(--ink);}

  .contact-list{position:absolute;left:23px;top:215px;margin:0;padding:0;list-style:none;}
  .contact-list li{display:flex;align-items:center;height:25.5px;font-size:17.5px;color:var(--text);}
  .contact-icon{width:14px;height:14px;margin-right:7px;flex:none;}
  .divider{position:absolute;left:23px;width:611px;top:324px;height:2px;background:var(--brand-blue);}
  .address{position:absolute;left:23px;top:331px;display:flex;align-items:center;font-size:17.5px;color:var(--text);margin:0;}
  .address .contact-icon{width:16px;height:16px;margin-right:8px;}
</style>
</head>
<body>
  <section class="card card--front">
    <div class="accent-bar"></div>
    <h1 class="person-name">Rui Matos</h1>
    <p class="person-role">Manager</p>

    <div class="brand"><span class="brand__dot"></span><span class="brand__name">VELTRANO</span></div>

    <ul class="contact-list">
      <li>
        <svg class="contact-icon" viewBox="0 0 14 14"><rect x="3" y="0.8" width="8" height="12.4" rx="1.4" fill="none" stroke="#1e9fda" stroke-width="1.4"/><circle cx="7" cy="11" r="0.8" fill="#1e9fda"/></svg>
        +351 912 480 375
      </li>
      <li>
        <svg class="contact-icon" viewBox="0 0 14 14"><path d="M3 1.5l2.2 2.6-1.1 1.6c.8 1.7 2.1 3 3.8 3.8l1.6-1.1 2.6 2.2-1.4 1.9C6.4 12.5 1.5 7.6 1.1 3z" fill="none" stroke="#1e9fda" stroke-width="1.3" stroke-linejoin="round"/></svg>
        +351 213 570 648
      </li>
      <li>
        <svg class="contact-icon" viewBox="0 0 14 14"><rect x="0.8" y="2.5" width="12.4" height="9" fill="#1e9fda"/><path d="M1 3l6 4.5L13 3" fill="none" stroke="#fff" stroke-width="1.1"/></svg>
        contacto@veltrano-auto.pt
      </li>
      <li>
        <svg class="contact-icon" viewBox="0 0 14 14"><rect x="0.5" y="0.5" width="13" height="13" rx="2" fill="#1e9fda"/></svg>
        www.veltrano-auto.pt/social
      </li>
    </ul>

    <div class="divider"></div>
    <p class="address">
      <svg class="contact-icon" viewBox="0 0 16 16"><path d="M8 1.5a3.6 3.6 0 0 0-3.6 3.6C4.4 8 8 11 8 11s3.6-3 3.6-5.9A3.6 3.6 0 0 0 8 1.5z" fill="none" stroke="#1e9fda" stroke-width="1.3"/><circle cx="8" cy="5.1" r="1.3" fill="#1e9fda"/><ellipse cx="8" cy="13.3" rx="5.5" ry="1.6" fill="none" stroke="#1e9fda" stroke-width="1.2"/></svg>
      Rua das Oliveiras, 42 Postal code: 1900-210 Lisboa
    </p>
  </section>

  <section class="card card--back">
    <div class="brand"><span class="brand__dot"></span><span class="brand__name">VELTRANO</span></div>
  </section>
</body>
</html>
```